Brenwo Tiling Solutions Needs A Web Design

We have been a sole trader but now started a new company. We need a web page designed around our new company. We are wall and floor tilers with over 20 years experience.
A Gold Coast family owned business, with over 20 years of experience, Dalton Krusey is proud to be a trusted name for all aspects of Wall and Floor Tiling Services servicing the Gold Coast to Brisbane, Tweed Heads to Mt Tamborine.

With an eye for detail we strive for perfection with the resources to work closely with designers, architects, contractors, and home owners, delivering the best possible service in wall and floor tiling.

We will be more than glad to provide our expertise and can consult or advice you to help you make the decisions that are right for you.

Renovations should always be seen as an investment not an expense. With an ultimate goal of utmost satisfaction, our trained and qualified tradesmen will provide you exceptional services. We are well equipped with latest tools and techniques to ensure that everything is done correctly with attention paid to the smallest details.
Updates

Hello I may not have been very clear. My husband Dalton Krusey is a tiler and we used just a basic PDF flyer "Company profile" when sending our quotations. He now has decided to use a company name and so I would like a web design page for this company "Brenwo Tiling Solutions Pty Ltd" I would like to use the information as stated (in the company profile PDF) BUT under the name Brenwo - I will look into a more detailed look into the description of the job and repost the details - unfortunately I will not be able to do sometime in the next 2 days. I will then repost. My apologies for this Thank You Mae-Lin Krusey

Target Market(s)

Our clients we are aiming at are Builders domestic(homes) and commercial (shops, duplexs & 3 storey units, resort pools) plus home owners looking to renovate existing tiled areas or lay new tiles to new homes. Internal pool and pool surround

Number of Pages Required

3 page

Font styles to use
Serif

Colors
9bcb3b
ec1f27
fbed22

Requirements
Must have
• We like fluro green and black colours. and use the name Dalton Krusey (the owner) as he does the tiling labour and is the one with the expertise.
• The final design should communicate professional workmanship. quality and expertise in ALL aspects of tiling,We have pride in our workmanship and do not cut corners so that the job is done right the first time to the correct standards. Our good name is our reputation.
• I have attached a logo which we would like in fluro green and black. The person in the logo has a hammer - we want to get rid of the hammer as that is for carpentry and we are floor tilers. If another tool ie mallet can be replaced. Can you do that?
Nice to have
• Photos - highlights stand out - nice borders. classic design.

```html
<!DOCTYPE html>
<html lang="en">
<head>
<meta charset="utf-8">
<title>Dalton Krusey Tiling</title>
<link rel="stylesheet" href="https://fonts.googleapis.com/css2?family=Open+Sans:wght@400;600;700&display=swap">
<style>
:root{
  --red:#e30613;
  --green:#9bcb3b;
  --nav:#2b2b2b;
  --ink:#2a2a2a;
  --muted:#666;
  --gallery:#4b4b4b;
  --review-bg:#f0f0f0;
  --footer:#212121;
  --footer-text:#bdbdbd;
  --input:#333;
}
*{box-sizing:border-box;margin:0;padding:0}
html,body{width:719px;height:1200px;overflow:hidden;background:#fff}
body{position:relative;font-family:"Open Sans",Arial,sans-serif;color:var(--ink)}
.abs{position:absolute}
.licence-badge{left:497px;top:0;width:124px;height:26px;background:var(--red);color:#fff;font-size:5.4px;font-weight:600;line-height:7.5px;padding:5px 0 0 13px}
.brand{left:254px;top:46px;width:200px;text-align:center;color:var(--red);font-weight:700;font-size:12px;letter-spacing:-.2px}
.main-nav{left:97px;top:82px;width:525px;height:23px;background:var(--nav);display:flex}
.main-nav a{color:#fff;font-size:6.4px;font-weight:600;text-decoration:none;display:flex;align-items:center;justify-content:center;border-right:1px solid #3c3c3c}
.main-nav a.active{background:var(--red)}
.hero-band{left:0;top:105px;width:719px;height:244px;background:#e6e6e6}
.hero-photo{left:97px;top:105px;width:525px;height:244px;background:linear-gradient(135deg,#2f3b30 0%,#5e6b5a 28%,#cfd3d8 48%,#e7e9ec 70%,#8c9bb0 100%)}
.hero-arrow{width:19px;height:19px;border-radius:50%;background:rgba(255,255,255,.55);top:220px}
.hero-caption{left:124px;background:rgba(40,40,40,.75);color:#fff;font-size:7px;font-weight:600;padding:0 6px;height:19px;line-height:19px}
.hero-shadow{left:100px;top:349px;width:519px;height:12px;background:radial-gradient(ellipse at top,rgba(0,0,0,.18),transparent 70%)}
.section-title{font-size:13px;font-weight:400;text-transform:uppercase;color:#333}
.welcome-photo{left:97px;top:426px;width:138px;height:145px;background:linear-gradient(160deg,#5a4a3a,#c89a4a 55%,#d8cfc0)}
.welcome-copy{left:250px;top:426px;width:210px;font-size:5.6px;line-height:9.9px;color:var(--muted)}
.btn{height:16px;line-height:16px;text-align:center;font-size:5.8px;color:#fff;font-weight:600}
.btn-dark{left:251px;top:555px;width:55px;background:#333}
.btn-green{left:310px;top:555px;width:56px;background:var(--green)}
.services-box{left:472px;top:426px;width:150px;height:145px;background:var(--red);padding:10px 0 0 11px}
.services-box li{list-style:none;color:#fff;font-size:5.7px;height:16.2px;position:relative;padding-left:10px}
.services-box li::before{content:"";position:absolute;left:0;top:2.3px;width:3px;height:3px;border-radius:50%;background:#fff}
.gallery-band{left:0;top:618px;width:719px;height:199px;background:repeating-linear-gradient(45deg,#4e4e4e 0 3px,#474747 3px 6px)}
.gallery-title{left:0;top:636px;width:719px;text-align:center;color:#fff;font-size:13px}
.thumb{top:670px;height:116px;border:2px solid #8a8a8a}
.gal-arrow{top:718px;width:17px;height:17px;border-radius:50%;background:#5f5f5f}
.reviews-band{left:0;top:817px;width:719px;height:196px;background:var(--review-bg)}
.reviews-title{left:0;top:841px;width:719px;text-align:center;font-size:13px;color:#333}
.review-card{top:878px;width:255px;height:88px;background:#fff}
.avatar{width:52px;height:52px;border-radius:50%;top:10px;left:14px;background:linear-gradient(#d9c2a8,#8f6a4e)}
.reviewer{top:69px;left:0;width:80px;text-align:center;font-size:5.6px;color:#555;letter-spacing:.3px}
.review-text{left:93px;top:14px;width:150px;font-size:5.6px;line-height:10.8px;color:#777}
.dot{top:980px;width:4px;height:4px;border-radius:50%;background:#ddd}
.site-footer{left:0;top:1013px;width:719px;height:187px;background:var(--footer)}
.foot-head{top:1034px;color:#ddd;font-size:6px;font-weight:600;letter-spacing:.2px}
.foot-text{font-size:5.7px;color:var(--footer-text);line-height:8.4px}
.foot-link{left:271px;font-size:5.7px;color:var(--footer-text)}
.rule{height:1px;background:#333;left:369px;width:118px}
.social{top:1141px;width:8px;height:8px;border-radius:50%;background:#9a9a9a}
.field{left:502px;width:120px;background:var(--input);color:#ccc;font-size:5px;padding:4px 4px}
.send{left:556px;top:1138px;width:66px;height:15px;background:var(--red);color:#fff;font-size:5px;text-align:center;line-height:15px;font-weight:600}
.copyright{left:0;top:1181px;width:719px;text-align:center;font-size:5.5px;color:#ccc}
.copyright span{color:var(--red)}
</style>
</head>
<body>

<div class="abs licence-badge">WALL AND FLOOR TILING SPECIALIST<br>ABN 00 112 334 556 - BSA LICENCE 10482</div>
<div class="abs brand">DALTON KRUSEY TILING</div>

<nav class="abs main-nav">
  <a class="active" style="width:60px">HOME</a>
  <a style="width:70px">ABOUT US</a>
  <a style="width:81px">OUR SERVICES</a>
  <a style="width:90px">WHY CHOOSE US</a>
  <a style="width:66px">REVIEWS</a>
  <a style="width:64px">GALLERY</a>
  <a style="width:94px;border-right:0">CONTACT US</a>
</nav>

<div class="abs hero-band" role="img" aria-label="White square wall tile pattern"></div>
<div class="abs hero-photo" role="img" aria-label="Photo of white marble tiled outdoor stairs beside a glass balustrade"></div>
<div class="abs hero-arrow" style="left:108px"><svg width="19" height="19"><path d="M11 5l-4 4.5 4 4.5" stroke="#444" stroke-width="1.5" fill="none"/></svg></div>
<div class="abs hero-arrow" style="left:593px"><svg width="19" height="19"><path d="M8 5l4 4.5-4 4.5" stroke="#fff" stroke-width="1.5" fill="none"/></svg></div>
<div class="abs hero-caption" style="top:286px">AENEAN ULLAMCORPER, NISL AC SOLLICITUDIN PULVINAR, ANTE ODIO PORTA</div>
<div class="abs hero-caption" style="top:305px">ANTE, SIT AMET ULTRICIES SEM TORTOR VITAE IPSUM.</div>
<div class="abs hero-shadow"></div>

<h2 class="abs section-title" style="left:97px;top:387px">Welcome to Dalton Krusey Tiles</h2>
<h2 class="abs section-title" style="left:467px;top:387px">Our Services</h2>

<div class="abs welcome-photo" role="img" aria-label="Photo of a tiled floor mosaic inside a shop"></div>
<p class="abs welcome-copy">A Gold Coast family owned business, with over 20 years of experience, Dalton Krusey Tiling is proud to be a trusted name for all aspects of Wall and Floor Tiling Services servicing the Gold Coast to Brisbane, Tweed Heads to Mt Tamborine. With an eye for detail we strive for perfection with the resources to work closely with designers, architects, contractors, and home owners, delivering the best possible service in wall and floor tiling. We will be more than glad to provide our expertise and can consult or advice you to help you make the decisions that are right for you. Renovations should always be seen as an investment not an expense. With an ultimate goal of utmost satisfaction, our trained and qualified tradesmen will provide you exceptional services. We are well equipped with latest tools and techniques to ensure that everything is done correctly with attention paid to the smallest details.</p>
<div class="abs btn btn-dark">Read More</div>
<div class="abs btn btn-green">Contact Now</div>

<ul class="abs services-box">
  <li>Wall and Floor Tiling – New or Renovations</li>
  <li>Ceramic</li>
  <li>Stone – Granite, Marble, Sandstone etc</li>
  <li>Glass Mosaics</li>
  <li>Driveways</li>
  <li>Swimming Pools, coping and pool surrounds</li>
  <li>Commercial and Residential tiling</li>
  <li>Waterproofing</li>
</ul>

<div class="abs gallery-band"></div>
<h2 class="abs gallery-title">OUR GALLERY</h2>
<div class="abs gal-arrow" style="left:64px"><svg width="17" height="17"><path d="M10 5l-3.5 3.5L10 12" stroke="#aaa" stroke-width="1.3" fill="none"/></svg></div>
<div class="abs gal-arrow" style="left:639px"><svg width="17" height="17"><path d="M7 5l3.5 3.5L7 12" stroke="#aaa" stroke-width="1.3" fill="none"/></svg></div>
<div class="abs thumb" style="left:97px;width:126px;background:linear-gradient(#2a2a2a 40%,#e8e8e8)" role="img" aria-label="Photo of a dark table on a polished tiled floor"></div>
<div class="abs thumb" style="left:232px;width:125px;background:linear-gradient(90deg,#3a3838,#6d6a68 60%,#d8d8d8)" role="img" aria-label="Photo of a dark tiled bathroom with toilet"></div>
<div class="abs thumb" style="left:364px;width:126px;background:linear-gradient(90deg,#3a6fb0,#e0a030 55%,#d43a1a)" role="img" aria-label="Photo of a column tiled in blue with orange and red stripes"></div>
<div class="abs thumb" style="left:496px;width:126px;background:linear-gradient(160deg,#1e8fe0,#0a5cc0 60%,#103a80)" role="img" aria-label="Photo of a blue tiled swimming pool"></div>

<div class="abs reviews-band"></div>
<h2 class="abs reviews-title">REVIEWS</h2>

<div class="abs review-card" style="left:98px">
  <div class="abs avatar" role="img" aria-label="Reviewer portrait"></div>
  <div class="abs reviewer">LIAM&amp;ROSA</div>
  <p class="abs review-text">We purchased a house just before xmas and thought our chances of getting a tiler straight after xmas may have been difficult. We contacted Dalton who arrived on time for his appointment and was able to start the tiling job on 28 December and 3 days and 80sqm of tiling</p>
</div>
<div class="abs review-card" style="left:367px">
  <div class="abs avatar" style="background:linear-gradient(#e08a6a,#8a3a2a)" role="img" aria-label="Reviewer portrait"></div>
  <div class="abs reviewer">KELBRIX</div>
  <p class="abs review-text">I have been using Krusey Tiling for a period of time and found it unique to find a business so focused on quality and customer service. Nothing is ever a bother and they always make sure time frames are met. I normally do not recommend people however Krusey Tiling is</p>
</div>
<div class="abs dot" style="left:351px;background:var(--green)"></div>
<div class="abs dot" style="left:358px"></div>
<div class="abs dot" style="left:365px"></div>

<footer class="abs site-footer"></footer>
<div class="abs foot-head" style="left:98px">ABOUT US</div>
<div class="abs foot-head" style="left:271px">USEFUL LINKS</div>
<div class="abs foot-head" style="left:369px">CONTACT INFO</div>
<div class="abs foot-head" style="left:502px">CONTACT NOW</div>

<p class="abs foot-text" style="left:98px;top:1058px;width:122px">Proin sollicitudin imperdiet orci, laoreet rhoncus diam feugiat eu. Maecenas hendrerit iaculis nisi et tristique. Vivamus non lacus ut nibh tempor dapibus. Vivamus sit amet auctor lorem. Lorem ipsum dolor sit amet, consectetur adipiscing elit.</p>
<div class="abs foot-text" style="left:177px;top:1138px">Read More &gt;&gt;</div>

<div class="abs foot-link" style="top:1058px">Home</div>
<div class="abs foot-link" style="top:1074px">About Us</div>
<div class="abs foot-link" style="top:1090px">Services</div>
<div class="abs foot-link" style="top:1106px">Gallery</div>
<div class="abs foot-link" style="top:1122px">Reviews</div>
<div class="abs foot-link" style="top:1138px">Contact</div>

<svg class="abs" style="left:368px;top:1059px" width="8" height="6"><rect x=".5" y=".5" width="7" height="5" fill="none" stroke="#ccc"/><path d="M.5 .5l3.5 3 3.5-3" fill="none" stroke="#ccc"/></svg>
<div class="abs foot-text" style="left:383px;top:1058px">d.krusey@mailbox.com.au</div>
<div class="abs rule" style="top:1072px"></div>
<svg class="abs" style="left:368px;top:1081px" width="7" height="7"><path d="M1 1.5C1 4.5 3 6.5 5.5 6.5l1-1.3-1.5-1-.8.7C3.2 4.4 2.6 3.8 2.3 3l.7-.8-1-1.5z" fill="#ccc"/></svg>
<div class="abs foot-text" style="left:383px;top:1080px">0400 555 019</div>
<div class="abs rule" style="top:1096px"></div>
<svg class="abs" style="left:368px;top:1107px" width="6" height="8"><path d="M3 8C1 5 0 4 0 3a3 3 0 016 0c0 1-1 2-3 5z" fill="#ccc"/><circle cx="3" cy="3" r="1" fill="#212121"/></svg>
<div class="abs foot-text" style="left:383px;top:1107px">14 Coral Reef Drive, Unit 3<br>Burleigh Heads, QLD 4220</div>

<div class="abs social" style="left:371px"></div>
<div class="abs social" style="left:390px"></div>
<div class="abs social" style="left:408px"></div>
<div class="abs social" style="left:427px"></div>
<div class="abs social" style="left:445px"></div>
<div class="abs social" style="left:464px"></div>

<div class="abs field" style="top:1059px;height:16px">Name</div>
<div class="abs field" style="top:1077px;height:15px">Email Address</div>
<div class="abs field" style="top:1094px;height:36px">Message</div>
<div class="abs send">SEND</div>

<div class="abs copyright">Copyright © 2016 - <span>yoursite</span></div>

</body>
</html>
```